Brindlecove (main name) sharpening systems(underneath)

Specializing in Knife, Scissors and Clipper sharpening, repair and maintenance.
I would like a logo designed that has at least one of the elements above showing what could happen as a result of the instrument being sharpened by my company as part of the logo (maybe the word Brindlecove being cut in half)

Target Market(s)

commercial (restaurants or any establishment that deals with food preparation, salons, barbershops) residential (any homes that use knives scissors or clippers)

Contact Information for Business Card

Name: Marcus Pellingham
Address: K240 Coral Vista Heights
Cell: 12465917362
Email: brindlecovehone@mailtrove.net

Requirements
Must have
• Brindlecove....sharpening systems clean front with strong logo indicating what we do as part of logo front of card
• Contact details: back of card
• we sharpen on site or pick up and drop off within 24hrs (at back of Card)
• telephone number: (at back) for contact
• address and other details (at back)

```html
<!DOCTYPE html>
<html lang="en">
<head>
<meta charset="utf-8">
<title>Brindlecove Sharpening Systems – Business Card</title>
<link rel="stylesheet" href="https://fonts.googleapis.com/css2?family=Cinzel:wght@500&family=Open+Sans:wght@400;700&display=swap">
<style>
  :root {
    --backdrop: #5b3f2d;
    --band: #929292;
    --face-top: #ffffff;
    --face-light: #f2f2f2;
    --face-mid: #c8c8c8;
    --face-bottom: #5f5f61;
    --ink: #1f1f1f;
    --ink-soft: #2b2b2b;
  }
  * { margin: 0; padding: 0; box-sizing: border-box; }
  html, body {
    width: 1200px;
    height: 1000px;
    overflow: hidden;
    background: var(--backdrop);
  }
  .canvas {
    position: relative;
    width: 1200px;
    height: 1000px;
  }
  .card {
    position: absolute;
    left: 266px;
    width: 666px;
    height: 397px;
    overflow: hidden;
    background: linear-gradient(to bottom,
      var(--face-top) 0%,
      var(--face-top) 14%,
      var(--face-light) 24%,
      var(--face-mid) 60%,
      var(--face-bottom) 100%);
    box-shadow: 0 4px 10px rgba(0,0,0,0.35);
    font-family: "Open Sans", Arial, sans-serif;
    color: var(--ink-soft);
    text-align: center;
  }
  .card--front { top: 74px; }
  .card--back  { top: 533px; }
  .card__band {
    position: absolute;
    top: 0; left: 0; right: 0;
    height: 36px;
    background: var(--band);
  }
  .brand-name {
    position: absolute;
    top: 148px;
    left: 0; right: 0;
    font-family: "Open Sans", Arial, sans-serif;
    font-weight: 700;
    font-size: 58px;
    line-height: 1;
    letter-spacing: 1px;
    color: var(--ink);
    text-transform: uppercase;
  }
  .brand-tagline {
    position: absolute;
    top: 290px;
    left: 0; right: 0;
    font-size: 17px;
  }
  .holder-name {
    position: absolute;
    top: 88px;
    left: 0; right: 0;
    font-family: "Cinzel", "Times New Roman", serif;
    font-weight: 500;
    font-size: 30px;
    letter-spacing: 0.5px;
    color: var(--ink);
  }
  .contact-icons {
    position: absolute;
    top: 168px;
    left: 0; right: 0;
    display: flex;
    justify-content: center;
    gap: 7px;
  }
  .contact-icons svg { width: 15px; height: 14px; fill: var(--ink); }
  .contact-line {
    position: absolute;
    left: 0; right: 0;
    font-size: 16.5px;
    line-height: 1;
  }
  .contact-line--phone   { top: 199px; }
  .contact-line--email   { top: 223px; }
  .contact-line--address { top: 257px; }
  .divider {
    position: absolute;
    top: 299px;
    left: 318px;
    width: 30px;
    height: 2px;
    background: var(--ink);
  }
  .service-note {
    position: absolute;
    top: 326px;
    left: 0; right: 0;
    font-size: 16.5px;
  }
</style>
</head>
<body>
<main class="canvas">

  <section class="card card--front">
    <div class="card__band"></div>
    <h1 class="brand-name">Brindlecove</h1>
    <p class="brand-tagline">Sharpening Systems</p>
  </section>

  <section class="card card--back">
    <div class="card__band"></div>
    <h2 class="holder-name">MARCUS PELLINGHAM</h2>
    <div class="contact-icons">
      <svg viewBox="0 0 16 14" aria-label="Phone" role="img">
        <path d="M1 4.5C1 2.5 4 1.5 8 1.5s7 1 7 3v1.3h-3.2V4.3H4.2v1.5H1z"/>
        <path d="M4 6.5h8l2 6H2z M6.2 8.2a1.8 1.8 0 1 0 3.6 0a1.8 1.8 0 1 0-3.6 0" fill-rule="evenodd"/>
      </svg>
      <svg viewBox="0 0 16 14" aria-label="Email" role="img">
        <path d="M1 2.5h14v1L8 8 1 3.5z"/>
        <path d="M1 5l7 4.5L15 5v7H1z"/>
      </svg>
      <svg viewBox="0 0 16 14" aria-label="Address" role="img">
        <path d="M8 1l7 6.2-1 1.1-1-0.9V13H9.7V9.5H6.3V13H3V7.4l-1 0.9-1-1.1z"/>
      </svg>
    </div>
    <p class="contact-line contact-line--phone">12465917362</p>
    <p class="contact-line contact-line--email">brindlecovehone@mailtrove.net</p>
    <p class="contact-line contact-line--address">K240 Coral Vista Heights</p>
    <div class="divider"></div>
    <p class="service-note">We sharpen on site or pick up and drop off within 24hrs</p>
  </section>

</main>
</body>
</html>
```